Handyman home maintenance postcard

We would like the postcard to state what we do : Painting, plumbing, electrical, flooring, carpentry, drywall, fencing, windows and more. We would also like our promotion to state : First four hours of work is only $299. Additional hours are 25% off our regular rate of $110 an hour. Rate includes two expert handymen working to complete your job.

Target Market(s)

30-75

Industry/Entity Type

Home maintenance

```html
<!DOCTYPE html>
<html lang="en">
<head>
<meta charset="utf-8">
<title>Steadfast Home Services – Postcard</title>
<link href="https://fonts.googleapis.com/css2?family=Poppins:wght@400;500;600;700;800&family=Roboto+Condensed:wght@600&display=swap" rel="stylesheet">
<style>
  :root{
    --stage:#3f3f3f;
    --paper:#f7f8fa;
    --navy:#27375c;
    --navy-panel:#223558;
    --navy-deep:#121c3a;
    --blue-accent:#4d6cb0;
    --orange:#fbab18;
    --orange-deep:#f27c0a;
    --ink:#3a3a3a;
    --rule:#9aa0ab;
    --white:#ffffff;
  }
  *{box-sizing:border-box;margin:0;padding:0}
  html,body{width:907px;height:1200px;overflow:hidden}
  body{background:var(--stage);font-family:"Poppins",sans-serif;position:relative}

  .card{position:absolute;left:46px;width:810px;height:540px;background:linear-gradient(135deg,#ffffff 0%,#eef0f4 55%,#f9fafb 100%);overflow:hidden;box-shadow:0 3px 8px rgba(0,0,0,.35)}
  .card--front{top:48px}
  .card--back{top:614px}

  /* front */
  .headline{position:absolute;left:28px;top:18px;font-weight:800;font-size:46px;line-height:56px;color:var(--navy);letter-spacing:-.5px}
  .headline .accent{color:var(--blue-accent)}
  .tagline{position:absolute;left:28px;top:139px;font-size:17px;color:#4a4a4a}
  .features{position:absolute;left:28px;top:176px;list-style:none}
  .feature{display:flex;align-items:center;height:37px;font-weight:500;font-size:16.5px;color:var(--ink)}
  .feature__icon{width:31px;height:31px;border-radius:50%;background:var(--orange);margin-right:15px;flex:none;display:flex;align-items:center;justify-content:center}
  .feature__text{border-bottom:1.5px solid #555;width:224px;line-height:36px}
  .feature:last-child .feature__text{border-bottom:none}
  .hero-art{position:absolute;left:372px;top:34px;width:420px;height:296px;border-radius:8px;background:radial-gradient(ellipse at 55% 45%,#3f5fb0 0%,#8ea3cf 40%,rgba(240,242,246,0) 72%);z-index:2}

  .services{position:absolute;left:0;top:299px;width:810px;height:128px;background:linear-gradient(180deg,var(--orange) 0%,var(--orange-deep) 100%)}
  .services__title{position:absolute;left:28px;top:9px;font-weight:700;font-size:16.5px;color:var(--white)}
  .services__list{position:absolute;left:24px;top:40px;width:780px;display:flex;list-style:none}
  .service{flex:1;display:flex;flex-direction:column;align-items:center;color:var(--white);font-weight:600;font-size:15px}
  .service svg{width:42px;height:42px;margin-bottom:8px}

  /* contact bar */
  .contact-bar{position:absolute;left:0;bottom:0;width:810px;height:111px;background:var(--white)}
  .contact-bar__panel{position:absolute;left:0;top:0;width:392px;height:111px;background:var(--navy-panel);clip-path:polygon(0 0,352px 0,392px 111px,0 111px)}
  .contact-bar__lower{position:absolute;left:0;top:61px;width:392px;height:50px;background:var(--navy-deep);clip-path:polygon(0 0,370px 0,392px 50px,0 50px)}
  .phone{position:absolute;left:18px;top:12px;display:flex;align-items:center;font-weight:800;font-size:43px;line-height:44px;color:var(--white);letter-spacing:.5px}
  .phone__icon{width:36px;height:36px;border-radius:50%;background:var(--orange);margin-right:9px;display:flex;align-items:center;justify-content:center}
  .details{position:absolute;left:18px;top:69px;list-style:none;font-size:11.5px;line-height:15px;color:var(--white)}
  .details li{display:flex;align-items:center}
  .details svg{width:11px;height:11px;margin-right:12px}
  .brand{position:absolute;left:420px;top:24px;display:flex;align-items:center}
  .brand__dot{width:54px;height:54px;border-radius:50%;background:var(--orange);margin-right:14px;flex:none}
  .brand__name{font-weight:700;font-size:29px;line-height:31px;color:#1b1b1b;letter-spacing:-.3px}

  /* back */
  .offer-panel{position:absolute;left:0;top:0;width:349px;height:427px;background:var(--navy-panel)}
  .offer-box{position:absolute;left:23px;top:20px;width:300px;height:89px;background:var(--orange);border-radius:4px;padding:6px 0 0 13px;font-weight:800;font-size:30px;line-height:36px;color:#111;letter-spacing:-.3px}
  .offer-detail{position:absolute;left:14px;top:122px;width:322px;text-align:center;font-weight:600;font-size:17.5px;line-height:21px;color:var(--white)}
  .offer-detail .hl{color:var(--orange)}
  .about{position:absolute;left:23px;top:226px;width:300px;color:var(--white);font-size:11.6px;line-height:13.5px;text-align:justify}
  .about__title{color:var(--orange);font-weight:700;font-size:11.5px;margin-bottom:0}
  .about p+p{margin-top:13.5px}
  .indicia{position:absolute;left:684px;top:29px;width:92px;height:110px;border:1px solid var(--rule);display:flex;align-items:center;justify-content:center;text-align:center;font-family:"Roboto Condensed",sans-serif;font-weight:600;font-size:13px;line-height:16.5px;color:#34405a}
  .address-line{position:absolute;left:431px;width:345px;height:1px;background:var(--rule)}
</style>
</head>
<body>

<section class="card card--front" aria-label="Postcard front">
  <h1 class="headline">Trusted Handyman<br>&amp; <span class="accent">Repair</span> Services</h1>
  <p class="tagline">Your Expert Go-To For Home Repairs.</p>
  <ul class="features">
    <li class="feature"><span class="feature__icon"><svg width="18" height="18" viewBox="0 0 20 20" fill="none" stroke="#fff" stroke-width="2.2"><circle cx="10" cy="10" r="7"/><path d="M10 6v4l3 2"/></svg></span><span class="feature__text">20+ years of experience</span></li>
    <li class="feature"><span class="feature__icon"><svg width="17" height="17" viewBox="0 0 20 20" fill="#fff"><rect x="2" y="9" width="4" height="9" rx="1"/><path d="M7 9l4-7c2 0 2.5 1.5 2 3l-1 3h5c1.2 0 2 1 1.7 2.2l-1.5 6C17 17.5 16 18 15 18H7z"/></svg></span><span class="feature__text">Reliable &amp; Quality Service</span></li>
    <li class="feature"><span class="feature__icon"><svg width="19" height="19" viewBox="0 0 20 20" fill="#fff"><circle cx="6" cy="6" r="3"/><circle cx="13" cy="6" r="3"/><path d="M1 16c0-4 2.5-6 5-6s5 2 5 6zM9 16c0-4 2-6 4-6s6 2 6 6z"/></svg></span><span class="feature__text">Skilled &amp; Trained Personel</span></li>
  </ul>

  <div class="hero-art" role="img" aria-label="Illustration of small workers climbing a giant blue cordless drill with hex nuts and a hammer"></div>

  <div class="services">
    <h2 class="services__title">WHAT WE DO :</h2>
    <ul class="services__list">
      <li class="service"><svg viewBox="0 0 40 40" fill="#fff"><path d="M22 4l14 14-8 6-12-12z"/><path d="M17 15l8 8-5 3-6-6z"/><path d="M14 22l4 4-9 10-5-5z"/></svg>Painting</li>
      <li class="service"><svg viewBox="0 0 40 40" fill="#fff"><rect x="4" y="3" width="12" height="4"/><rect x="7" y="7" width="6" height="14"/><rect x="7" y="17" width="22" height="6"/><rect x="24" y="17" width="6" height="16"/><rect x="21" y="33" width="12" height="4"/></svg>Plumbing</li>
      <li class="service"><svg viewBox="0 0 40 40" fill="none" stroke="#fff" stroke-width="3.5"><circle cx="20" cy="20" r="16"/><path d="M15 12v7M25 12v7M12 19h16v4a8 8 0 0 1-16 0zM20 31v5"/></svg>Electrical</li>
      <li class="service"><svg viewBox="0 0 40 40" fill="#fff"><path d="M8 18h11v8H5zM21 18h11l3 8H21zM4 28h15v9H2zM21 28h15l2 9H21z"/><path d="M12 4l1.5 3.5L17 9l-3.5 1.5L12 14l-1.5-3.5L7 9l3.5-1.5zM27 3l1 2.5 2.5 1-2.5 1-1 2.5-1-2.5-2.5-1 2.5-1z"/></svg>Flooring</li>
      <li class="service"><svg viewBox="0 0 40 40" fill="#fff"><path d="M20 6a14 14 0 0 1 14 14H6A14 14 0 0 1 20 6z"/><circle cx="20" cy="26" r="10"/><rect x="4" y="19" width="32" height="3" fill="#f69012"/></svg>Carpentry</li>
      <li class="service"><svg viewBox="0 0 40 40" fill="#fff"><rect x="13" y="2" width="14" height="4"/><path d="M17 6h6v24l-3 8-3-8z"/><path d="M14 11l12 3v2l-12-3zM14 17l12 3v2l-12-3zM14 23l12 3v2l-12-3z"/></svg>Drywall</li>
      <li class="service"><svg viewBox="0 0 40 40" fill="#fff"><rect x="2" y="12" width="36" height="3"/><rect x="2" y="27" width="36" height="3"/><rect x="3" y="5" width="4" height="31"/><rect x="10" y="5" width="4" height="31"/><rect x="17" y="5" width="4" height="31"/><rect x="24" y="5" width="4" height="31"/><rect x="31" y="5" width="4" height="31"/></svg>Fencing</li>
      <li class="service"><svg viewBox="0 0 40 40" fill="#fff"><rect x="4" y="3" width="32" height="4"/><rect x="7" y="9" width="12" height="12"/><rect x="21" y="9" width="12" height="12"/><rect x="7" y="23" width="12" height="11"/><rect x="21" y="23" width="12" height="11"/><rect x="4" y="35" width="32" height="3"/></svg>Windows</li>
    </ul>
  </div>

  <footer class="contact-bar">
    <div class="contact-bar__panel"></div>
    <div class="contact-bar__lower"></div>
    <div class="phone"><span class="phone__icon"><svg width="20" height="20" viewBox="0 0 24 24" fill="#27375c"><path d="M6.6 10.8a15 15 0 0 0 6.6 6.6l2.2-2.2c.3-.3.7-.4 1-.2 1.1.4 2.3.6 3.6.6.6 0 1 .4 1 1V20c0 .6-.4 1-1 1A17 17 0 0 1 3 4c0-.6.4-1 1-1h3.5c.6 0 1 .4 1 1 0 1.3.2 2.5.6 3.6.1.3 0 .7-.2 1z"/></svg></span>310 555 0187</div>
    <ul class="details">
      <li><svg viewBox="0 0 12 12"><path d="M6 0a4.5 4.5 0 0 1 4.5 4.5C10.5 8 6 12 6 12S1.5 8 1.5 4.5A4.5 4.5 0 0 1 6 0z" fill="#fbab18"/><circle cx="6" cy="4.5" r="1.6" fill="#121c3a"/></svg>4170 Maple Grove Ave, #210, Los Angeles, California, 90000</li>
      <li><svg viewBox="0 0 12 12"><circle cx="6" cy="6" r="6" fill="#fbab18"/><rect x="3" y="4" width="6" height="4.2" fill="none" stroke="#121c3a" stroke-width="1"/><path d="M3 4l3 2.3L9 4" fill="none" stroke="#121c3a" stroke-width="1"/></svg>hello@steadfasthomeservices.com</li>
    </ul>
    <div class="brand"><span class="brand__dot"></span><span class="brand__name">Steadfast Home<br>Services</span></div>
  </footer>
</section>

<section class="card card--back" aria-label="Postcard back">
  <div class="offer-panel">
    <p class="offer-box">First four hours of work is only $299.</p>
    <p class="offer-detail">Additional hours are <span class="hl">25% off</span> our regular rate of <span class="hl">$110 an hour</span>. Rate includes two expert handymen working to complete your job.</p>
    <div class="about">
      <h3 class="about__title">Who We Are</h3>
      <p>Steadfast Home Services strives to be your go-to for home repairs. We have many years of experience in all facets of home repair and maintenance. Whether you are looking to repair that running toilet, replace that tired looking floor or give your home’s exterior or interior a fresh new color, we can get it done for you. On time, neatly and at a reasonable price.</p>
      <p>Our expert craftsmen can complete all kinds of projects while treating you and your home with respect &amp; care. We pride ourselves on doing your job properly the first time.</p>
    </div>
  </div>

  <div class="indicia">PRSRTSTD<br>ECRWSS<br>U.S.POSTAGE<br>PAID</div>
  <div class="address-line" style="top:215px"></div>
  <div class="address-line" style="top:269px"></div>
  <div class="address-line" style="top:319px"></div>
  <div class="address-line" style="top:373px"></div>

  <footer class="contact-bar">
    <div class="contact-bar__panel"></div>
    <div class="contact-bar__lower"></div>
    <div class="phone"><span class="phone__icon"><svg width="20" height="20" viewBox="0 0 24 24" fill="#27375c"><path d="M6.6 10.8a15 15 0 0 0 6.6 6.6l2.2-2.2c.3-.3.7-.4 1-.2 1.1.4 2.3.6 3.6.6.6 0 1 .4 1 1V20c0 .6-.4 1-1 1A17 17 0 0 1 3 4c0-.6.4-1 1-1h3.5c.6 0 1 .4 1 1 0 1.3.2 2.5.6 3.6.1.3 0 .7-.2 1z"/></svg></span>310 555 0187</div>
    <ul class="details">
      <li><svg viewBox="0 0 12 12"><path d="M6 0a4.5 4.5 0 0 1 4.5 4.5C10.5 8 6 12 6 12S1.5 8 1.5 4.5A4.5 4.5 0 0 1 6 0z" fill="#fbab18"/><circle cx="6" cy="4.5" r="1.6" fill="#121c3a"/></svg>4170 Maple Grove Ave, #210, Los Angeles, California, 90000</li>
      <li><svg viewBox="0 0 12 12"><circle cx="6" cy="6" r="6" fill="#fbab18"/><rect x="3" y="4" width="6" height="4.2" fill="none" stroke="#121c3a" stroke-width="1"/><path d="M3 4l3 2.3L9 4" fill="none" stroke="#121c3a" stroke-width="1"/></svg>hello@steadfasthomeservices.com</li>
    </ul>
    <div class="brand"><span class="brand__dot"></span><span class="brand__name">Steadfast Home<br>Services</span></div>
  </footer>
</section>

</body>
</html>
```